Business card design for new eCommerce site focusing on integrity and strong businsess tactics

We need a business card that will stand out and be memorable. Something with color that matches our company logo colors. Think high end version of Dealvine. There are 2 logos provided. The parent company is called Bright Harbor Ventures and we are presenting a new and very exciting eCommerce site called KeenTraders.example.

Target Market(s)

Our target markets are in the Activities, Food and Beverage, Health and Beauty

Industry/Entity Type

Marketing

Contact Information for Business Card

We have 4 members that need cards...I will provide all info to the winner of the design contest
Business Address is
48730 West 61st Avenue, Suite C204
Phoenix AZ 85917

Font styles to use
Serif
Sans Serif

Colors

Designer to choose colors to be used in the design.

Requirements
Must have
• The card must be memorable...should be unique in design but must exude integrity and be playful .
• I have provided several colors or our parent company...please feel free to use which ever
Nice to have
• I will leave this up to you. Feel free to use other images of your choosing that wraps around our client.....Activities, Dining, Health, Beauty
Should not have
• just dont be boring

```html
<!DOCTYPE html>
<html lang="en">
<head>
<meta charset="utf-8">
<title>Bright Harbor Ventures – Business Card</title>
<link href="https://fonts.googleapis.com/css2?family=Montserrat:wght@400;600;700&display=swap" rel="stylesheet">
<style>
  :root{
    --bg:#1b1c1e;
    --card-white:#ffffff;
    --brand-blue:#2e7db5;
    --brand-blue-dark:#256a9c;
    --brand-green:#8dc63f;
    --text-grey:#555a60;
    --rule-grey:#b5b8bc;
  }
  *{margin:0;padding:0;box-sizing:border-box}
  html,body{width:1200px;height:963px;overflow:hidden;background:var(--bg);font-family:'Montserrat',sans-serif}
  .stage{position:relative;width:1200px;height:963px;display:flex;align-items:center;justify-content:center;gap:50px}
  .card{position:relative;width:530px;height:300px;border-radius:16px;overflow:hidden;box-shadow:0 18px 40px rgba(0,0,0,.55)}

  /* front */
  .card-front{background:linear-gradient(160deg,#eef0f1 0%,var(--card-white) 45%)}
  .front-band{position:absolute;left:0;top:0;width:530px;height:300px}
  .front-decor{position:absolute;right:10px;top:120px;width:150px;height:160px;border-radius:50%;background:radial-gradient(circle,rgba(141,198,63,.14),rgba(141,198,63,0) 70%)}
  .brand-mark{position:absolute;left:40px;top:70px;display:flex;align-items:center;gap:12px}
  .brand-dot{width:22px;height:22px;border-radius:50%;background:var(--brand-green)}
  .brand-name{font-weight:700;font-size:23px;color:var(--brand-green);letter-spacing:.2px}
  .front-rule{position:absolute;left:40px;right:40px;top:158px;height:1px;background:var(--rule-grey)}
  .address{position:absolute;left:40px;top:170px;font-size:12.5px;line-height:1.5;color:var(--text-grey)}
  .person{position:absolute;right:40px;top:108px;text-align:right}
  .person-name{font-size:20px;font-weight:600;color:var(--brand-blue);line-height:1.2}
  .person-name .surname{color:var(--brand-green)}
  .person-role{font-size:13px;color:var(--text-grey);margin-top:1px}
  .contact{position:absolute;right:40px;top:170px;font-size:12px;line-height:1.6;color:var(--text-grey);text-align:right}
  .contact-line{display:flex;align-items:center;justify-content:flex-end;gap:8px}
  .contact-line svg{width:11px;height:11px}

  /* back */
  .card-back{background:linear-gradient(200deg,var(--brand-blue-dark) 0%,var(--brand-blue) 60%,#3587c0 100%)}
  .back-decor{position:absolute;left:60px;top:-30px;width:240px;height:330px;border-radius:45%;background:radial-gradient(ellipse,rgba(20,70,110,.28),rgba(20,70,110,0) 70%)}
  .back-brand{position:absolute;left:90px;top:170px;color:#f2f4f6}
  .back-name{display:flex;align-items:center;gap:12px;font-size:30px;font-weight:600}
  .back-dot{width:24px;height:24px;border-radius:50%;background:#f2f4f6}
  .tagline{font-size:13px;letter-spacing:.6px;margin:6px 0 0 36px}
  .back-url{font-size:12.5px;letter-spacing:.4px;margin:3px 0 0 36px}
</style>
</head>
<body>
<main class="stage">
  <section class="card card-front">
    <div class="front-decor" role="img" aria-label="Faint leafy tree decoration"></div>
    <svg class="front-band" viewBox="0 0 530 300">
      <path d="M0 236 H160 C188 236 192 282 226 282 H530 V300 H0 Z" fill="var(--brand-blue)"/>
      <path d="M178 252 C196 274 204 278 228 278 H530" fill="none" stroke="var(--brand-green)" stroke-width="5"/>
    </svg>
    <div class="brand-mark">
      <span class="brand-dot"></span>
      <span class="brand-name">Bright Harbor Ventures</span>
    </div>
    <div class="front-rule"></div>
    <p class="address">48730 West 61st Avenue,<br>Suite C204 Phoenix AZ 85917</p>
    <div class="person">
      <p class="person-name">Daniel <span class="surname">Reyes</span></p>
      <p class="person-role">Founder</p>
    </div>
    <div class="contact">
      <p class="contact-line">0400 555 018
        <svg viewBox="0 0 12 12"><rect x="3" y="0.5" width="6" height="11" rx="1" fill="none" stroke="var(--brand-blue)" stroke-width="1.2"/></svg></p>
      <p class="contact-line">info@keentraders.example
        <svg viewBox="0 0 12 12"><rect x="0.5" y="2.5" width="11" height="7" fill="var(--brand-blue)"/><path d="M0.5 2.5 L6 7 L11.5 2.5" fill="none" stroke="#fff" stroke-width="1"/></svg></p>
      <p class="contact-line">www.keentraders.example
        <svg viewBox="0 0 12 12"><circle cx="5" cy="5" r="3.6" fill="none" stroke="var(--brand-blue)" stroke-width="1.6"/><path d="M7.6 7.6 L11 11" stroke="var(--brand-blue)" stroke-width="1.8"/></svg></p>
    </div>
  </section>

  <section class="card card-back">
    <div class="back-decor" role="img" aria-label="Faint large figure decoration"></div>
    <div class="back-brand">
      <p class="back-name"><span class="back-dot"></span>KeenTraders.example</p>
      <p class="tagline">Activities-Dining-Health-Beauty</p>
      <p class="back-url">www.brightharborventures.example</p>
    </div>
  </section>
</main>
</body>
</html>
```